Rest. Build. Thrive. Book Cover

I would like a book cover for the print edition book I am self publishing. My cover will require front, back, and spine design. I have provided a template to assist with sizing and spacing.

My book is named "Rest. Build. Thrive. A Hands-On Diet, Drive to Act, and Attitude Handbook Building Energy Toward Stronger Vitality and Balance" by Gregory Halvorsen RD, CPT. I use the concept of waves as an analogy for forward progress in life and would like that reflected in the cover design. I would like the color scheme to be blacks, whites, grey, and various shades of blue. I have provided a style guide for reference. Please include my logo on the front, spine, and back of the design. Please include an about the author, book summary, and my picture on the back. I have provided the wording below.

About the Author: Gregory Halvorsen is a Registered Dietitian and Certified Personal Trainer from Cleveland, OH. He graduated from the Westbrook Valley University and currently works as a health coach in the healthcare industry. His passions are fitness, nutrition, science, and motivation. He has extensive knowledge and experience in wellness, healthcare, and disease treatment and disease. Gregory has worked with hundreds of people through counseling, consulting, and coaching in an effort to make a difference in their long-term health. In his spare time, he enjoys exercising, watching movies, and trying out new foods.

Book Summary: Believe in you. Trust in You. Rest. Build. Thrive. is a book committed to you. Behavior change and improved health can be challenging. You must feel empowered to make decisions and changes create momentum in the right direction. But, you may not always have the knowledge to do that. This book provides you with practical and fun tools and tips to improve your nutrition, motivation to move, and mindset. You are awesome. You are beautiful. You have the power to control your destiny and future. All you have to do is Rest, Build, and Thrive!

Please use a modern/ futuristic font style for the title. I have also provided some draft book covers for inspiration/ direction. Thank you!

Colors

Designer to choose only greyscale colors for use in the design.

Requirements
Must have
• Color scheme, about author, profile picture, and book summary on back, wave themed graphics

```html
<!DOCTYPE html>
<html lang="en">
<head>
<meta charset="utf-8">
<title>Rest. Build. Thrive. – Book Cover</title>
<link rel="stylesheet" href="https://fonts.googleapis.com/css2?family=Arimo:wght@400;700&family=Lobster&display=swap">
<style>
  :root {
    --back-slate: #53616a;
    --spine-slate: #2a3540;
    --sky-dark: #12191d;
    --sky-mid: #3a454d;
    --cloud-light: #e6ecef;
    --rock-grey: #727d83;
    --rock-dark: #1c2124;
    --heading-cream: #fdf5c9;
    --body-white: #ffffff;
    --title-ink: #2f3336;
    --brand-blue: #0fb6f5;
    --wave-light: #bfe9fb;
    --frame-line: #2c353b;
  }
  * { margin: 0; padding: 0; box-sizing: border-box; }
  html, body { width: 1200px; height: 906px; overflow: hidden; background: var(--back-slate); }
  .cover { position: relative; width: 1200px; height: 906px; font-family: "Arimo", Arial, sans-serif; }

  .back-panel { position: absolute; left: 0; top: 0; width: 564px; height: 906px; background: var(--back-slate); }
  .section-heading {
    position: absolute; left: 60px; font-family: "Lobster", cursive;
    font-weight: 400; font-size: 28px; color: var(--heading-cream);
  }
  .summary-heading { top: 86px; }
  .author-heading { top: 328px; }
  .summary-text {
    position: absolute; left: 62px; top: 133px; width: 413px;
    font-size: 13.2px; line-height: 15.4px; color: var(--body-white); text-align: justify;
  }
  .author-block {
    position: absolute; left: 62px; top: 322px; width: 414px;
    font-size: 13.4px; line-height: 15.4px; color: var(--body-white);
  }
  .author-photo {
    float: right; width: 129px; height: 126px; margin: 0 0 4px 14px;
    border: 1px solid #222; background: linear-gradient(160deg, #d8d8d8 0%, #8c8c8c 55%, #3a3a3a 100%);
  }
  .author-text { padding-top: 52px; }
  .blank-box {
    position: absolute; left: 323px; top: 728px; width: 220px; height: 132px;
    border: 1px solid var(--frame-line);
  }

  .spine { position: absolute; left: 564px; top: 0; width: 72px; height: 906px; background: var(--spine-slate); }

  .front-panel { position: absolute; left: 636px; top: 0; width: 564px; height: 906px; overflow: hidden; }
  .front-sky {
    position: absolute; left: 0; top: 0; width: 564px; height: 262px;
    background: linear-gradient(180deg, var(--sky-dark) 0%, #1f292f 45%, var(--sky-mid) 100%);
  }
  .front-landscape {
    position: absolute; left: 0; top: 262px; width: 564px; height: 644px;
    background: linear-gradient(180deg, var(--cloud-light) 0%, #c3cbd0 30%, var(--rock-grey) 62%, var(--rock-dark) 100%);
  }
  .wave-lines { position: absolute; left: 0; top: 470px; width: 564px; height: 260px; }
  .brand-mark {
    position: absolute; left: 80px; top: 130px; display: flex; align-items: center; gap: 14px;
    font-weight: 700; font-size: 92px; line-height: 1; letter-spacing: 6px; color: var(--brand-blue);
  }
  .brand-square { width: 26px; height: 26px; background: var(--brand-blue); }
  .book-title {
    position: absolute; right: 80px; top: 279px; text-align: right;
    font-weight: 400; font-size: 17.4px; line-height: 20.6px; color: var(--title-ink);
  }
  .author-byline {
    position: absolute; right: 22px; top: 814px;
    font-size: 20.6px; color: var(--body-white);
  }
</style>
</head>
<body>
<main class="cover">
  <section class="back-panel">
    <h2 class="section-heading summary-heading">Book Summary</h2>
    <p class="summary-text">Believe in you. Trust in You. Rest. Build. Thrive. is a book committed to you. Behavior change and improved health can be challenging. You must feel empowered to make decisions and changes create momentum in the right direction. But, you may not always have the knowledge to do that. This book provides you with practical and fun tools and tips to improve your nutrition, motivation to move, and mindset. You are awesome. You are beautiful. You have the power to control your destiny and future. All you have to do is Rest, Build, and Thrive!</p>

    <h2 class="section-heading author-heading">About the Author</h2>
    <div class="author-block">
      <div class="author-photo" role="img" aria-label="Black and white portrait of author Gregory Halvorsen"></div>
      <p class="author-text">Gregory Halvorsen is a Registered Dietitian and Certified Personal Trainer from Cleveland, OH. He graduated from the Westbrook Valley University and currently works as a health coach in the healthcare industry. His passions are fitness, nutrition, science, and motivation. He has extensive knowledge and experience in wellness, healthcare, and disease treatment and disease. Gregory has worked with hundreds of people through counseling, consulting, and coaching in an effort to make a difference in their long-term health. In his spare time, he enjoys exercising, watching movies, and trying out new foods.</p>
    </div>

    <div class="blank-box"></div>
  </section>

  <div class="spine"></div>

  <section class="front-panel">
    <div class="front-sky" role="img" aria-label="Dark stormy cloud sky"></div>
    <div class="front-landscape" role="img" aria-label="Black and white photo of jagged mountain peaks rising through clouds"></div>
    <svg class="wave-lines" viewBox="0 0 564 260" aria-hidden="true">
      <path d="M0 60 C 70 20, 140 100, 210 60 S 350 20, 420 60 S 530 100, 564 70" fill="none" stroke="var(--wave-light)" stroke-width="2" opacity="0.55"/>
      <path d="M0 110 C 70 70, 140 150, 210 110 S 350 70, 420 110 S 530 150, 564 120" fill="none" stroke="var(--brand-blue)" stroke-width="2.5" opacity="0.6"/>
      <path d="M0 160 C 70 120, 140 200, 210 160 S 350 120, 420 160 S 530 200, 564 170" fill="none" stroke="var(--wave-light)" stroke-width="1.5" opacity="0.4"/>
    </svg>
    <div class="brand-mark"><span class="brand-square"></span><span>RBT</span></div>
    <h1 class="book-title">REST. BUILD. THRIVE. :<br>A Hands-On Diet, Drive to Act,<br>and Attitude Handbook Building<br>Energy Toward Stronger<br>Vitality &amp; Balance</h1>
    <p class="author-byline">Gregory Halvorsen RD, CPT</p>
  </section>
</main>
</body>
</html>
```